Modern design for a watersports website

Building a brand new site for Kiteboarders/Kitesurfers .... this is the first of 8 sites we're rolling out.

We're as much looking for a partner to work with, and they will be chosen based on the winner of this site design.

It will need these menu pages:

1) How-To
2) Classifieds
3) Groups
4) News
5) Events

Width: 1150px

The home page, should feature:

1) A search box to enter a location
2) Under that, a series of boxes showing up to 5 previous locations chosen - these should be "buttons", directly under the location (i.e. no photo, just the location name)
3) Under that, a 5 x 3 grid of adverts, featuring a photo, a title & a price
4) Under that, top 5 headlines, each one featuring photo, headline & Summary
5) Under that, top 10 Group topics: Group, Title, Author, #Replies (no photo for these)
6) Under that, 5 x 3 grid of photos
7) Footer

Colours should be of the ocean:
Blues, greens, compatible with yellow. (i.e. not washed out blues like tellora), vibrant blues, but not too vivid as to overpower.

Avoid: Photos of any equipment, as they will date quickly.

Building

1 page

Sans Serif

• Ocean colours; blues
• Modern design

```html
<!DOCTYPE html>
<html lang="en">
<head>
<meta charset="utf-8">
<title>Swellkite.com</title>
<link href="https://fonts.googleapis.com/css2?family=Oswald:wght@400&family=Open+Sans:wght@400;600;700&display=swap" rel="stylesheet">
<style>
:root{
  --blue:#2b7bd6;
  --green:#4c9a0e;
  --orange:#f39a0b;
  --dark:#2e2e2e;
  --darker:#141414;
  --text:#333;
  --muted:#555;
  --line:#dcdcdc;
  --bg:#ededed;
}
*{box-sizing:border-box;margin:0;padding:0}
html,body{width:817px;height:1200px;overflow:hidden}
body{background:var(--bg);font-family:"Open Sans",sans-serif;color:var(--text);position:relative}
.page{position:absolute;left:53px;top:0;width:711px;height:1200px;background:#fff}
.abs{position:absolute}
.topbar{left:0;top:0;width:711px;height:32px;background:#f4f4f4;border-top:3px solid var(--blue);border-bottom:1px solid #e2e2e2;font-size:10px;color:#666}
.topbar .social{left:12px;top:9px;display:flex;gap:10px;font-size:9px;color:#888}
.topbar .social span:first-child{color:var(--blue)}
.topbar .account{right:13px;top:9px}
.brand{left:12px;top:44px;font-weight:700;font-size:33px;color:var(--blue);letter-spacing:-.5px;line-height:1}
.brand small{display:block;text-align:right;font-size:13px;color:var(--blue);margin-top:2px}
.search{left:484px;top:57px;width:213px;height:23px;border:1px solid #d5d5d5;font-size:10px;color:#666;padding:4px 7px}
.search svg{position:absolute;right:6px;top:5px}
.nav{left:0;top:109px;width:711px;height:35px;background:var(--dark);border-bottom:3px solid var(--blue);display:flex;color:#fff;font-size:11.5px}
.nav .home{width:51px;background:var(--blue);display:flex;align-items:center;justify-content:center}
.nav .item{display:flex;align-items:center;justify-content:center;border-right:1px solid #444}
.heading{display:flex;align-items:center;font-family:"Oswald",sans-serif;font-size:13px;height:16px}
.heading::after{content:"";flex:1;height:7px;margin-left:6px;background:repeating-linear-gradient(135deg,#d4d4d4 0 1px,transparent 1px 3px)}
.h-green{color:var(--green)} .h-orange{color:var(--orange)} .h-dark{color:#444}
.box{background:#fff;border:1px solid var(--line);box-shadow:0 1px 2px rgba(0,0,0,.08)}
.b-green{border-bottom:3px solid var(--green)}
.b-orange{border-bottom:3px solid var(--orange)}
.b-blue{border-bottom:3px solid var(--blue)}
.locations{display:grid;grid-template-columns:1fr 1fr;row-gap:9px;padding:9px 16px;font-size:10px;color:var(--muted)}
.locations li{list-style:none;display:flex;align-items:center;gap:7px;height:12px}
.dot{width:7px;height:7px;position:relative}
.dot i{position:absolute;width:2.5px;height:2.5px;border-radius:50%;background:var(--blue)}
.photo{display:block}
.ad{position:absolute;top:11px;width:156px}
.ad .photo{height:85px}
.ad h3{font-size:10px;color:var(--orange);font-weight:700;margin:8px 3px 2px}
.ad p{font-size:11.5px;color:#444;margin-left:3px}
.post{position:absolute;top:11px;width:206px}
.post .photo{height:102px}
.post h3{font-size:10px;color:var(--blue);font-weight:700;margin:11px 2px 1px}
.post p{font-size:9.5px;color:var(--muted);line-height:14px;margin-left:2px}
.btn{display:inline-block;font-family:"Oswald",sans-serif;color:#fff;font-size:13px;padding:2px 11px;margin:9px 0 0 0}
.btn-blue{background:var(--blue)} .btn-green{background:var(--green)}
.pager{left:191px;top:212px;display:flex;gap:6px}
.pager i{width:9px;height:9px;border-radius:50%;background:#444}
.pager i:first-child{background:var(--blue)}
.gallery .photo{position:absolute;width:92px;height:71px}
table{border-collapse:collapse;font-size:9.8px;color:#222;position:absolute;left:8px;top:8px}
th{font-family:"Oswald",sans-serif;font-weight:400;font-size:12.5px;color:#555;text-align:left;height:22px;vertical-align:top}
td{height:21.3px}
.footer{left:0;top:1054px;width:711px;height:118px;background:var(--dark);border-top:6px solid var(--blue);color:#fff}
.footer h4{font-family:"Oswald",sans-serif;font-weight:400;font-size:14px}
.about{left:10px;top:12px;width:215px}
.about p{font-size:9.6px;line-height:12px;margin-top:5px;letter-spacing:.2px}
.fbrand{left:252px;top:50px;width:208px;text-align:right;font-weight:700;font-size:29px;line-height:1;color:#fff}
.fbrand small{display:block;font-size:12px;margin-top:4px}
.follow{left:497px;top:12px;width:200px}
.icons{display:flex;gap:21px;margin-top:20px}
.icons .sq{width:29px;height:29px;background:#fff;display:flex;align-items:center;justify-content:center;font-weight:700;font-size:15px;color:#222}
.icons .sq.blue{background:var(--blue);color:#fff}
.copy{left:0;top:1172px;width:711px;height:28px;background:var(--darker);color:#ccc;font-size:9.5px;text-align:center;line-height:28px}
.copy b{color:#fff}
</style>
</head>
<body>
<div class="page">
  <div class="abs topbar">
    <div class="abs social"><span>tellora</span><span>Chirply</span><span>Linkwise</span></div>
    <div class="abs account">Register &nbsp;|&nbsp; Login</div>
  </div>

  <div class="abs brand">SWELLKITE<small>.COM</small></div>
  <div class="abs search">Search location here...
    <svg width="11" height="11" viewBox="0 0 11 11"><circle cx="4.5" cy="4.5" r="3.5" fill="none" stroke="#888" stroke-width="1.3"/><line x1="7" y1="7" x2="10" y2="10" stroke="#888" stroke-width="1.5"/></svg>
  </div>

  <nav class="abs nav">
    <div class="home"><svg width="17" height="15" viewBox="0 0 17 15"><path d="M8.5 1 L1 8 H3 V14 H7 V10 H10 V14 H14 V8 H16 Z" fill="#fff"/></svg></div>
    <div class="item" style="width:113px">How-To</div>
    <div class="item" style="width:107px">Classifieds</div>
    <div class="item" style="width:99px">Groups</div>
    <div class="item" style="width:82px">News</div>
    <div class="item" style="width:88px;border:none">Events</div>
  </nav>

  <div class="abs heading h-green" style="left:13px;top:159px;width:684px">LOCATION HERE</div>
  <ul class="abs box b-green locations" style="left:10px;top:183px;width:689px;height:88px">
    <li><span class="dot"><i style="left:0;top:2px"></i><i style="left:4px;top:0"></i><i style="left:4px;top:4px"></i></span>Lorem Ipsum is simply dummy text</li>
    <li><span class="dot"><i style="left:0;top:2px"></i><i style="left:4px;top:0"></i><i style="left:4px;top:4px"></i></span>Lorem Ipsum is simply dummy text</li>
    <li><span class="dot"><i style="left:0;top:2px"></i><i style="left:4px;top:0"></i><i style="left:4px;top:4px"></i></span>Lorem Ipsum is simply dummy text</li>
    <li><span class="dot"><i style="left:0;top:2px"></i><i style="left:4px;top:0"></i><i style="left:4px;top:4px"></i></span>Lorem Ipsum is simply dummy text</li>
    <li><span class="dot"><i style="left:0;top:2px"></i><i style="left:4px;top:0"></i><i style="left:4px;top:4px"></i></span>Lorem Ipsum is simply dummy text</li>
    <li><span class="dot"><i style="left:0;top:2px"></i><i style="left:4px;top:0"></i><i style="left:4px;top:4px"></i></span>Lorem Ipsum is simply dummy text</li>
  </ul>

  <div class="abs heading h-orange" style="left:13px;top:287px;width:684px">Adverts</div>
  <div class="abs box b-orange" style="left:10px;top:310px;width:689px;height:145px">
    <div class="ad" style="left:10px"><div class="photo" role="img" aria-label="Surfer riding inside a large curling wave" style="background:linear-gradient(160deg,#6f86a8,#2e4a78 60%,#c9d4e3)"></div><h3>Lorem Ipsum is simply</h3><p>$14.00</p></div>
    <div class="ad" style="left:180px"><div class="photo" role="img" aria-label="Kiteboarder carving across turquoise water" style="background:linear-gradient(135deg,#cfe9e4,#3fb5a8 55%,#1c7c78)"></div><h3>Lorem Ipsum is simply</h3><p>$14.00</p></div>
    <div class="ad" style="left:350px"><div class="photo" role="img" aria-label="Kitesurfer on the water under a deep blue sky" style="background:linear-gradient(180deg,#3d64b4,#5f8bd0 65%,#8aa9c9)"></div><h3>Lorem Ipsum is simply</h3><p>$14.00</p></div>
    <div class="ad" style="left:520px"><div class="photo" role="img" aria-label="Rider leaving a spray trail across green water" style="background:linear-gradient(135deg,#5b7a3a,#3e6b36 50%,#8fae78)"></div><h3>Lorem Ipsum is simply</h3><p>$14.00</p></div>
  </div>

  <div class="abs heading h-dark" style="left:13px;top:471px;width:503px">Latest Post</div>
  <div class="abs box b-blue" style="left:10px;top:494px;width:454px;height:236px">
    <div class="post" style="left:11px"><div class="photo" role="img" aria-label="Kiteboarder airborne above the sea against a dark blue sky" style="background:linear-gradient(180deg,#1e3f86,#2d56a3 70%,#8b9cb4)"></div><h3>Lorem Ipsum is simply dummy text</h3><p>Lorem Ipsum is simply dummy text of the printing and typesetting industry.</p><span class="btn btn-blue">Read More</span></div>
    <div class="post" style="left:231px"><div class="photo" role="img" aria-label="Kitesurfer riding across turquoise sea" style="background:linear-gradient(180deg,#4b9fbf,#2f8ea8 60%,#6fbcc4)"></div><h3>Lorem Ipsum is simply dummy text</h3><p>Lorem Ipsum is simply dummy text of the printing and typesetting industry.</p><span class="btn btn-blue">Read More</span></div>
    <div class="abs pager"><i></i><i></i><i></i></div>
  </div>

  <div class="abs heading h-green" style="left:488px;top:471px;width:209px">Gallery</div>
  <div class="abs box b-green gallery" style="left:485px;top:494px;width:213px;height:236px">
    <div class="photo" role="img" aria-label="Kiteboarder jumping over a beach" style="left:6px;top:7px;background:linear-gradient(180deg,#c7d8ec,#8fb3d6 70%,#d9cfb8)"></div>
    <div class="photo" role="img" aria-label="Rider crossing deep blue water" style="left:112px;top:7px;background:linear-gradient(180deg,#5c8a63,#1e4f8c 45%,#143f78)"></div>
    <div class="photo" role="img" aria-label="Rider in shallow turquoise water" style="left:6px;top:93px;background:linear-gradient(180deg,#e6eef5,#7fc1bb 60%,#3e9d96)"></div>
    <div class="photo" role="img" aria-label="Kitesurfer on a grey blue sea" style="left:112px;top:93px;background:linear-gradient(180deg,#9eb1c4,#6d86a1 60%,#b8c3cc)"></div>
    <span class="btn btn-green abs" style="left:69px;top:183px;margin:0;padding:3px 17px">View All</span>
  </div>

  <div class="abs heading h-orange" style="left:13px;top:748px;width:681px">Group Discussion</div>
  <div class="abs box b-orange" style="left:10px;top:771px;width:686px;height:250px">
    <table>
      <colgroup><col style="width:114px"><col style="width:327px"><col style="width:128px"><col style="width:60px"></colgroup>
      <tr><th>Group</th><th>Title</th><th>Author</th><th>Replies</th></tr>
      <tr><td>Group name</td><td>Lorem Ipsum is simply dummy text of the printing and industry.</td><td>Lorem Ipsum</td><td>1</td></tr>
      <tr><td>Group name</td><td>Lorem Ipsum is simply dummy text of the printing and industry.</td><td>Lorem Ipsum</td><td>2</td></tr>
      <tr><td>Group name</td><td>Lorem Ipsum is simply dummy text of the printing and industry.</td><td>Lorem Ipsum</td><td>50</td></tr>
      <tr><td>Group name</td><td>Lorem Ipsum is simply dummy text of the printing and industry.</td><td>Lorem Ipsum</td><td>10</td></tr>
      <tr><td>Group name</td><td>Lorem Ipsum is simply dummy text of the printing and industry.</td><td>Lorem Ipsum</td><td>6</td></tr>
      <tr><td>Group name</td><td>Lorem Ipsum is simply dummy text of the printing and industry.</td><td>Lorem Ipsum</td><td>7</td></tr>
      <tr><td>Group name</td><td>Lorem Ipsum is simply dummy text of the printing and industry.</td><td>Lorem Ipsum</td><td>2</td></tr>
      <tr><td>Group name</td><td>Lorem Ipsum is simply dummy text of the printing and industry.</td><td>Lorem Ipsum</td><td>7</td></tr>
      <tr><td>Group name</td><td>Lorem Ipsum is simply dummy text of the printing and industry.</td><td>Lorem Ipsum</td><td>0</td></tr>
      <tr><td>Group name</td><td>Lorem Ipsum is simply dummy text of the printing and industry.</td><td>Lorem Ipsum</td><td>6</td></tr>
    </table>
  </div>

  <div class="abs" style="left:0;top:1046px;width:711px;height:8px;background:#e4e4e4"></div>
  <footer class="abs footer">
    <div class="abs about"><h4>About</h4><p>Lorem Ipsum is simply dummy text of the printing and typesetting industry. Lorem Ipsum has been the industry's standard dummy text ever since the 1500s, when an unknown printer took a galley of type and scrambled it to make a type specimen book.</p></div>
    <div class="abs fbrand">SWELLKITE<small>.COM</small></div>
    <div class="abs follow"><h4>Follow Us</h4>
      <div class="icons">
        <div class="sq blue" aria-label="tellora">t</div>
        <div class="sq" aria-label="Chirply">C</div>
        <div class="sq" aria-label="Linkwise">L</div>
        <div class="sq" aria-label="Email"><svg width="17" height="12" viewBox="0 0 17 12"><rect x="0.5" y="0.5" width="16" height="11" fill="#222"/><path d="M1 1 L8.5 7 L16 1" fill="none" stroke="#fff" stroke-width="1.4"/></svg></div>
      </div>
    </div>
  </footer>
  <div class="abs copy">© <b>Swellkite.com</b> - 2015. All Rights reserved.</div>
</div>
</body>
</html>
```